BrightArc Orthodontics appointment card design

I need appointment cards/ business cards made. Front will be Logo, name, title, email, phone number and location (5327 Varden Hollow Blvd, Ste 412, Concord, NC 28027) . the back should have an appointment card (name, time, date) and also 3 addresses listed with a check box so we can check to which location they are going.
Wendell Pratt Orthodontics
- 6315 Elmore Street, Ste 514, Harrisburg, NC 28075
- 3761 Tessaly Drive NE, Ste 118, Concord, NC 28025
- 2194 Quarrow Medical Drive, Ste 605, Charlotte, NC 28277
Business card can be horizontal or vertical in Design.
I need to be able to edit it to update and add new employees

Requirements
Must have
• Front:
• - Logo
• - Name & Title (able to be edited)
• - phone (704-555-0148) & Email (need to be able to edit)
• - Address: 5327 Varden Hollow Blvd, Ste 412
• Concord, NC 28027
• Back:
• Appointment Card design:
• - Name, time, Date
• - 3 locations w/ a check box so the patient knows where to go:
• Wendell Pratt Orthodontics
• - 6315 Elmore Street, Ste 514, Harrisburg, NC 28075
• - 3761 Tessaly Drive NE, Ste 118, Concord, NC 28025
• - 2194 Quarrow Medical Drive, Ste 605, Charlotte, NC 28277

```html
<!DOCTYPE html>
<html lang="en">
<head>
<meta charset="utf-8">
<title>BrightArc Orthodontics – Appointment &amp; Business Card</title>
<link rel="stylesheet" href="https://fonts.googleapis.com/css2?family=Roboto:wght@400;500;700&display=swap">
<style>
  :root {
    --brand-blue: #1284c7;
    --brand-blue-dark: #0f6fae;
    --band-gray: #6f7072;
    --ink: #3b3b3b;
    --ink-soft: #555;
    --line: #444;
    --card: #ffffff;
    --backdrop: #5a5b5e;
  }
  * { box-sizing: border-box; margin: 0; padding: 0; }
  html, body { width: 1200px; height: 1000px; overflow: hidden; }
  body {
    background: radial-gradient(ellipse at 50% 30%, #6a6b6e 0%, var(--backdrop) 55%, #3f4043 100%);
    font-family: "Roboto", Arial, sans-serif;
    position: relative;
  }
  .card {
    position: absolute;
    left: 250px;
    width: 700px;
    height: 400px;
    background: var(--card);
    border-radius: 28px;
    overflow: hidden;
    box-shadow: 0 14px 30px rgba(0,0,0,.35);
  }
  .card--back { top: 60px; }
  .card--front { top: 530px; }

  /* shared brand name */
  .brand-name {
    font-family: "Roboto", Arial, sans-serif;
    font-weight: 700;
    color: var(--brand-blue);
    line-height: 1.05;
    display: flex;
    align-items: center;
    gap: 10px;
  }
  .brand-dot {
    border-radius: 50%;
    background: var(--brand-blue);
    flex: none;
  }

  /* ---------- back: appointment card ---------- */
  .top-strip {
    position: absolute; top: 0; left: 0; right: 0; height: 16px;
    background: var(--brand-blue);
  }
  .appt-title {
    position: absolute; left: 46px; top: 48px;
    font-size: 21px; font-weight: 700; color: var(--brand-blue);
  }
  .back-brand {
    position: absolute; right: 42px; top: 92px;
    font-size: 27px; width: 230px;
  }
  .back-brand .brand-dot { width: 16px; height: 16px; }
  .field {
    position: absolute;
    display: flex; align-items: flex-end; gap: 8px;
    font-size: 14px; color: var(--ink-soft);
  }
  .field .rule { flex: 1; border-bottom: 1.2px solid var(--line); height: 1px; margin-bottom: 3px; }
  .field--name { left: 46px; top: 100px; width: 360px; }
  .field--date { left: 46px; top: 140px; width: 360px; }
  .field--time { left: 46px; top: 200px; width: 608px; }
  .field--time .rule--lead { flex: 0 0 250px; }
  .ampm {
    position: absolute; right: 46px; top: 238px;
    display: flex; gap: 18px; font-size: 14px; color: var(--ink-soft);
  }
  .checkbox {
    display: inline-block; width: 15px; height: 15px;
    border: 1.6px solid var(--brand-blue); background: #fff;
    vertical-align: -2px; margin-right: 5px;
  }
  .practice-name {
    position: absolute; left: 250px; top: 232px;
    font-size: 19px; font-weight: 700; color: var(--brand-blue);
  }
  .practice-name span { font-size: 15px; font-weight: 400; color: var(--ink-soft); }
  .location {
    position: absolute; text-align: center;
    font-size: 13px; line-height: 1.35; color: var(--ink-soft);
  }
  .location .checkbox { display: block; margin: 0 auto 6px; }
  .location--1 { left: 34px; top: 244px; width: 190px; }
  .location--2 { left: 250px; top: 284px; width: 220px; }
  .location--3 { left: 470px; top: 318px; width: 220px; }

  /* ---------- front: business card ---------- */
  .front-brand {
    position: absolute; left: 48px; top: 52px;
    font-size: 44px; width: 340px;
  }
  .front-brand .brand-dot { width: 22px; height: 22px; }
  .bands { position: absolute; left: 0; top: 0; }
  .person {
    position: absolute; left: 64px; top: 196px; color: #fff;
  }
  .person__name { font-size: 22px; font-weight: 700; letter-spacing: .5px; }
  .person__title { font-size: 15px; font-weight: 400; margin-top: 2px; }
  .front-address {
    position: absolute; left: 52px; top: 292px;
    font-size: 16px; line-height: 1.4; color: var(--ink);
  }
  .contact {
    position: absolute; right: 40px; bottom: 34px;
    text-align: right; font-size: 16px; line-height: 1.7; color: var(--ink);
  }
  .contact__row { display: flex; align-items: center; justify-content: flex-end; gap: 8px; }
  .contact__row svg { width: 14px; height: 14px; }
</style>
</head>
<body>

  <!-- Appointment side -->
  <section class="card card--back" aria-label="Appointment card">
    <div class="top-strip"></div>
    <h2 class="appt-title">Next Appointment</h2>

    <div class="field field--name"><span>Name</span><span class="rule"></span></div>
    <div class="field field--date"><span>Date</span><span class="rule"></span></div>
    <div class="field field--time"><span class="rule rule--lead"></span><span>Time</span><span class="rule"></span></div>

    <div class="brand-name back-brand"><span class="brand-dot"></span>BrightArc Orthodontics</div>

    <div class="ampm">
      <span><i class="checkbox"></i>AM</span>
      <span><i class="checkbox"></i>PM</span>
    </div>

    <p class="practice-name">Wendell Pratt <span>Orthodontics</span></p>

    <div class="location location--1"><i class="checkbox"></i>6315 Elmore Street, Ste 514,<br>Harrisburg, NC 28075</div>
    <div class="location location--2"><i class="checkbox"></i>3761 Tessaly Drive NE, Ste 118,<br>Concord, NC 28025</div>
    <div class="location location--3"><i class="checkbox"></i>2194 Quarrow Medical Drive,<br>Ste 605, Charlotte, NC 28277</div>
  </section>

  <!-- Business card side -->
  <section class="card card--front" aria-label="Business card">
    <div class="brand-name front-brand"><span class="brand-dot"></span>BrightArc Orthodontics</div>

    <svg class="bands" width="700" height="400" viewBox="0 0 700 400" aria-hidden="true">
      <polygon points="0,182 440,182 400,272 0,272" fill="var(--brand-blue)"/>
      <polygon points="450,182 700,182 700,292 404,292" fill="var(--band-gray)"/>
    </svg>

    <div class="person">
      <div class="person__name">WENDELL PRATT</div>
      <div class="person__title">Orthodontics</div>
    </div>

    <address class="front-address" style="font-style:normal">
      5327 Varden Hollow Blvd,<br>Ste 412 - Concord, NC 28027
    </address>

    <div class="contact">
      <div class="contact__row">704-555-0148
        <svg viewBox="0 0 16 16"><path d="M4 1.5l2.2 3-1.3 1.6a8 8 0 0 0 5 5l1.6-1.3 3 2.2-1.4 2.4C7.5 14.6 1.4 8.5 1.6 2.9z" fill="var(--brand-blue)"/></svg>
      </div>
      <div class="contact__row">wendell.pratt@brightarcmail.com
        <svg viewBox="0 0 16 16"><rect x="1" y="3" width="14" height="10" rx="1.5" fill="var(--brand-blue)"/><path d="M1.5 4l6.5 5 6.5-5" fill="none" stroke="#fff" stroke-width="1.3"/></svg>
      </div>
    </div>
  </section>

</body>
</html>
```